Packaging sleeve for Kraft Box

I need an urgent sleeve made for my box. I have the logo , business name and slogan. I have all the nutritional values and ingredients.for you to get an idea.
Luxurious item with colours like gold, cream, browns I have included some colour ideas and pictures of my marshmallows
The box measures 125x125x75mm
The sleeve will be 55mm
we sell award winning gourmet marshmallows.
These are very light and delecate.
There are 4 flavours which will need to be included on the sleeve. The box is Kraft material
The font I would like you to use is "Milasian Circa for the 4 flavours which are.
Rosewater & Strawberry ( needs 2 star award logo placed by the name.)
Dark Chocolate & Vanilla (needs 1 star award placed by the name)
Chocolate Orange
Crispy Salted Caramel

Target Market(s)

Luxury adult both male and female

Industry/Entity Type

Food Store

Font styles to use
Script
Other font styles liked:
• Milasian Circa

Requirements
Must have
• Colours that work with the logo colours and Kraft Box.
• Logo, business name and slogan need to be in gold
• Elegant simple design
Nice to have
• Delicate decorative swirl pattern on parts of the sleeve
• Try and use some colours behind the flavour names to reflect the marshmallow flavours i.e rose colour for the rosewater and brown for chocolate, orange for the orange chocolate and so on.
Should not have
• Busy patterns or clip art.

```html
<!DOCTYPE html>
<html lang="en">
<head>
<meta charset="utf-8">
<title>Hazel's Marshmallows – Box Sleeve Colourways</title>
<link rel="stylesheet" href="https://fonts.googleapis.com/css2?family=Great+Vibes&family=Kaushan+Script&display=swap">
<style>
  :root {
    --page: #ffffff;
    --rose: #be8a7e;
    --mocha: #9e7064;
    --cocoa: #673f35;
    --gold: #e0b64a;
    --cream: #ffffff;
    --tone-light: rgba(255, 240, 230, 0.16);
    --tone-gold: rgba(214, 160, 80, 0.16);
    --fold: rgba(255, 255, 255, 0.18);
  }
  * { margin: 0; padding: 0; box-sizing: border-box; }
  html, body {
    width: 1200px; height: 849px; overflow: hidden;
    background: var(--page);
  }
  .sheet { position: relative; width: 1200px; height: 849px; }

  .sleeve {
    position: absolute; left: 45px; width: 1110px; height: 221px;
    overflow: hidden; color: var(--cream);
  }
  .sleeve--rose  { top: 65px;  background: var(--rose); }
  .sleeve--mocha { top: 311px; background: var(--mocha); }
  .sleeve--cocoa { top: 562px; background: var(--cocoa); }

  .pattern-area {
    position: absolute; top: 0; bottom: 0;
    background: linear-gradient(120deg, var(--tone-gold), var(--tone-light) 55%, transparent);
  }
  .pattern-area--left { left: 0; width: 302px; }
  .pattern-area--right {
    left: 808px; right: 0;
    background: linear-gradient(240deg, var(--tone-gold), var(--tone-light) 55%, transparent);
  }

  .fold { position: absolute; top: 0; bottom: 0; width: 1px; background: var(--fold); }
  .fold--left { left: 302px; }
  .fold--right { left: 808px; }

  .frame {
    position: absolute; left: 18px; top: 10px; right: 15px; bottom: 11px;
    border: 2px solid var(--cream); border-radius: 12px;
    box-shadow: 2px 2px 0 0 var(--gold), inset 2px 2px 0 0 var(--gold);
  }

  .tagline {
    position: absolute;
    font-family: "Great Vibes", cursive;
    font-size: 46px; line-height: 76px; font-weight: 700;
    color: var(--cream);
    text-shadow: 2px 2px 0 var(--gold);
    white-space: nowrap;
  }
  .tagline--left {
    left: 53px; top: 32px;
    writing-mode: vertical-rl;
    height: 170px;
  }
  .tagline--right {
    left: 882px; top: 204px;
    transform: rotate(-90deg); transform-origin: 0 0;
    width: 170px;
  }

  .brand-name {
    position: absolute; left: 0; right: 0; top: 40px;
    text-align: center;
    font-family: "Kaushan Script", cursive;
    font-size: 28px; line-height: 36px;
    color: var(--cream);
  }

  .brand-square {
    position: absolute; left: 437px; top: 89px; width: 73px; height: 70px;
    border: 2px solid var(--cream); border-radius: 4px;
  }

  .flavours {
    position: absolute; left: 529px; top: 86px;
    list-style: none;
    font-family: "Kaushan Script", cursive;
    font-size: 13px; line-height: 20.5px;
    color: var(--cream);
  }
  .award-stars { color: var(--gold); font-size: 9px; margin-left: 3px; vertical-align: 3px; }

  .slogan {
    position: absolute; left: 0; right: 0; top: 174px;
    text-align: center;
    font-family: "Kaushan Script", cursive;
    font-size: 20px; line-height: 26px;
    color: var(--cream);
  }
</style>
</head>
<body>
<main class="sheet">

  <section class="sleeve sleeve--rose">
    <div class="pattern-area pattern-area--left" role="img" aria-label="Delicate gold and cream swirl pattern"></div>
    <div class="pattern-area pattern-area--right" role="img" aria-label="Delicate gold and cream swirl pattern"></div>
    <span class="fold fold--left"></span><span class="fold fold--right"></span>
    <div class="frame"></div>
    <p class="tagline tagline--left">Velvet<br>Clouds</p>
    <h2 class="brand-name">Hazel's Marshmallows</h2>
    <span class="brand-square"></span>
    <ul class="flavours">
      <li>Rosewater &amp; Strawberry<span class="award-stars">★★</span></li>
      <li>Dark Chocolate &amp; Vanilla<span class="award-stars">★</span></li>
      <li>Chocolate Orange</li>
      <li>Crispy Salted Caramel</li>
    </ul>
    <p class="slogan">Award Winning Marshmallows</p>
    <p class="tagline tagline--right">Velvet<br>Clouds</p>
  </section>

  <section class="sleeve sleeve--mocha">
    <div class="pattern-area pattern-area--left" role="img" aria-label="Delicate gold and cream swirl pattern"></div>
    <div class="pattern-area pattern-area--right" role="img" aria-label="Delicate gold and cream swirl pattern"></div>
    <span class="fold fold--left"></span><span class="fold fold--right"></span>
    <div class="frame"></div>
    <p class="tagline tagline--left">Velvet<br>Clouds</p>
    <h2 class="brand-name">Hazel's Marshmallows</h2>
    <span class="brand-square"></span>
    <ul class="flavours">
      <li>Rosewater &amp; Strawberry<span class="award-stars">★★</span></li>
      <li>Dark Chocolate &amp; Vanilla<span class="award-stars">★</span></li>
      <li>Chocolate Orange</li>
      <li>Crispy Salted Caramel</li>
    </ul>
    <p class="slogan">Award Winning Marshmallows</p>
    <p class="tagline tagline--right">Velvet<br>Clouds</p>
  </section>

  <section class="sleeve sleeve--cocoa">
    <div class="pattern-area pattern-area--left" role="img" aria-label="Delicate gold and cream swirl pattern"></div>
    <div class="pattern-area pattern-area--right" role="img" aria-label="Delicate gold and cream swirl pattern"></div>
    <span class="fold fold--left"></span><span class="fold fold--right"></span>
    <div class="frame"></div>
    <p class="tagline tagline--left">Velvet<br>Clouds</p>
    <h2 class="brand-name">Hazel's Marshmallows</h2>
    <span class="brand-square"></span>
    <ul class="flavours">
      <li>Rosewater &amp; Strawberry<span class="award-stars">★★</span></li>
      <li>Dark Chocolate &amp; Vanilla<span class="award-stars">★</span></li>
      <li>Chocolate Orange</li>
      <li>Crispy Salted Caramel</li>
    </ul>
    <p class="slogan">Award Winning Marshmallows</p>
    <p class="tagline tagline--right">Velvet<br>Clouds</p>
  </section>

</main>
</body>
</html>
```